Business Card, Letterhead, Fax Cover and Envelopes
Golden Harbor Insurance Services
Professional
Martin Brantley
PO Box 7162
Riverside, CA 92871
martin@goldenharborins.example
www.goldenharborins.example
License #KT51294
I would like a cutting edge design that will provide a visual impact while maintaining a professional, corporate look.
Empowering Businesses and Families Through Innovative Insurance Solutions

```html
<!DOCTYPE html>
<html lang="en">
<head>
<meta charset="utf-8">
<title>Golden Harbor Insurance Services – Stationery</title>
<link href="https://fonts.googleapis.com/css2?family=Open+Sans:wght@400;600;700&display=swap" rel="stylesheet">
<style>
  :root{
    --bg:#ececec;
    --paper:#ffffff;
    --navy:#0d3f86;
    --blue:#1f5fb8;
    --sky:#4f8fd9;
    --ink:#3a3f47;
    --muted:#8a9099;
    --line:#d5d9df;
  }
  *{box-sizing:border-box;margin:0;padding:0}
  html,body{width:1200px;height:314px;overflow:hidden;background:var(--bg);font-family:"Open Sans",Arial,sans-serif;color:var(--ink)}
  .set{position:relative;width:1200px;height:314px}
  .piece{position:absolute;background:var(--paper);overflow:hidden;border:1px solid var(--line)}
  .brand{display:flex;align-items:center;gap:5px;color:var(--navy);font-weight:700;line-height:1.05;text-transform:uppercase}
  .brand .dot{flex:none;background:var(--blue)}
  .brand-name{font-size:7px;letter-spacing:.02em;white-space:nowrap}
  .swoosh{position:absolute;right:0;top:0}
  .small{font-size:4px;line-height:1.45;color:var(--muted);white-space:nowrap}
  .hero-brand{position:absolute;left:12px;top:12px}
  .hero-brand .brand-name{font-size:13px}
  .hero-brand .dot{width:22px;height:22px}
  .hero-brand .tag{font-size:7px;color:var(--muted);font-weight:400;text-transform:none;margin-top:3px}

  .card{width:122px;height:70px}
  .card .brand{position:absolute;left:8px;top:10px}
  .card .brand-name{font-size:6px}
  .card .brand .dot{width:9px;height:9px}
  .card .person{position:absolute;left:8px;bottom:8px}
  .card .person b{display:block;font-size:5px;color:var(--navy)}
  .card.back .info{position:absolute;right:8px;top:12px;text-align:right}
  .card.back .info b{display:block;font-size:5.5px;color:var(--navy)}
  .card.centered .brand{left:50%;top:50%;transform:translate(-50%,-50%);flex-direction:column;text-align:center}
  .card.blue{background:linear-gradient(135deg,var(--blue),var(--navy));border-color:var(--navy)}
  .card.blue .brand{color:#fff;left:50%;top:50%;transform:translate(-50%,-50%);flex-direction:column;text-align:center}
  .card.blue .brand .dot{background:#fff}

  .letter{width:200px;height:252px}
  .letter .brand{position:absolute;left:14px;top:14px}
  .letter .brand .dot{width:12px;height:12px}
  .letter .contact{position:absolute;left:31px;top:34px}
  .letter .foot{position:absolute;left:0;right:50px;bottom:8px;text-align:center}
  .letter .faint{position:absolute;left:60px;top:105px;width:80px;height:50px;border-radius:50%;background:radial-gradient(ellipse,#eef2f8,transparent 70%)}

  .env{width:230px;height:76px}
  .env .brand{position:absolute;left:10px;top:9px}
  .env .brand .dot{width:10px;height:10px}
  .env .return{position:absolute;left:10px;top:26px}

  .open-env{width:238px;height:118px}
  .open-env .flap{position:absolute;left:0;top:0}
</style>
</head>
<body>
<main class="set">

  <div class="hero-brand brand">
    <span class="dot"></span>
    <div><div class="brand-name">Golden Harbor</div><div class="tag">Insurance Services</div></div>
  </div>

  <section class="piece card front" style="left:10px;top:100px">
    <svg class="swoosh" width="122" height="70" viewBox="0 0 122 70"><path d="M122 0 V70 H112 C120 50 118 22 96 0Z" fill="var(--navy)"/><path d="M96 0 C116 20 118 48 110 70 H104 C112 46 108 22 88 0Z" fill="var(--sky)"/></svg>
    <div class="brand"><span class="dot"></span><span class="brand-name">Golden Harbor<br>Insurance Services</span></div>
    <div class="person small"><b>Martin Brantley</b>License #KT51294</div>
  </section>

  <section class="piece card back" style="left:145px;top:100px">
    <div class="info small"><b>Martin Brantley</b>PO Box 7162<br>Riverside, CA 92871<br>martin@goldenharborins.example<br>www.goldenharborins.example</div>
  </section>

  <section class="piece card centered" style="left:10px;top:180px">
    <div class="brand"><span class="dot"></span><span class="brand-name">Golden Harbor<br>Insurance Services</span></div>
  </section>

  <section class="piece card blue" style="left:145px;top:180px">
    <div class="brand"><span class="dot"></span><span class="brand-name">Golden Harbor<br>Insurance Services</span></div>
  </section>

  <section class="piece letter" style="left:283px;top:12px">
    <svg class="swoosh" width="200" height="252" viewBox="0 0 200 252"><path d="M200 0 V252 H192 C200 160 196 60 140 0Z" fill="var(--navy)"/><path d="M140 0 C190 50 196 150 188 252 H182 C190 150 180 60 128 0Z" fill="var(--sky)"/></svg>
    <div class="brand"><span class="dot"></span><span class="brand-name">Golden Harbor<br>Insurance Services</span></div>
    <div class="faint"></div>
    <div class="foot small">PO Box 7162 · Riverside, CA 92871 · www.goldenharborins.example</div>
  </section>

  <section class="piece letter" style="left:497px;top:12px">
    <svg class="swoosh" width="200" height="252" viewBox="0 0 200 252"><path d="M200 0 V252 H192 C200 160 196 60 140 0Z" fill="var(--navy)"/><path d="M140 0 C190 50 196 150 188 252 H182 C190 150 180 60 128 0Z" fill="var(--sky)"/></svg>
    <div class="brand"><span class="dot"></span><span class="brand-name">Golden Harbor<br>Insurance Services</span></div>
    <div class="contact small">Martin Brantley<br>PO Box 7162<br>Riverside, CA 92871<br>martin@goldenharborins.example</div>
    <div class="faint"></div>
    <div class="foot small">License #KT51294</div>
  </section>

  <section class="piece env" style="left:705px;top:80px">
    <svg class="swoosh" width="230" height="76" viewBox="0 0 230 76"><path d="M230 0 V76 H218 C230 50 222 20 196 0Z" fill="var(--navy)"/><path d="M196 0 C222 20 228 52 214 76 H207 C220 50 210 20 186 0Z" fill="var(--sky)"/></svg>
    <div class="brand"><span class="dot"></span><span class="brand-name">Golden Harbor<br>Insurance Services</span></div>
    <div class="return small">PO Box 7162<br>Riverside, CA 92871</div>
  </section>

  <section class="piece env" style="left:705px;top:170px">
    <svg class="swoosh" width="230" height="76" viewBox="0 0 230 76"><path d="M230 0 V76 H218 C230 50 222 20 196 0Z" fill="var(--navy)"/><path d="M196 0 C222 20 228 52 214 76 H207 C220 50 210 20 186 0Z" fill="var(--sky)"/></svg>
    <div class="brand"><span class="dot"></span><span class="brand-name">Golden Harbor<br>Insurance Services</span></div>
    <div class="return small">PO Box 7162<br>Riverside, CA 92871</div>
  </section>

  <section class="piece open-env" style="left:952px;top:28px">
    <svg class="flap" width="238" height="118" viewBox="0 0 238 118"><path d="M0 0 H238 L119 62Z" fill="var(--navy)"/><path d="M0 0 L119 62 L238 0 V8 L119 70 L0 8Z" fill="var(--sky)"/><path d="M0 118 L119 62 L238 118" fill="none" stroke="var(--line)"/></svg>
  </section>

  <section class="piece open-env" style="left:952px;top:160px">
    <svg class="flap" width="238" height="118" viewBox="0 0 238 118"><path d="M0 0 H238 L119 62Z" fill="#f4f6f9" stroke="var(--line)"/><path d="M0 118 L119 62 L238 118" fill="none" stroke="var(--line)"/></svg>
  </section>

</main>
</body>
</html>
```